I need a logo design and a business card design for a new strategy consultancy that I set up called Tessaron LLC. We help clients make strategically important decisions, cutting through the cloud of noise. The design should imply clarity, simplicity and wisdom.

```html
<!DOCTYPE html>
<html lang="en">
<head>
<meta charset="UTF-8">
<title>Tessaron LLC — Business Cards</title>
<link href="https://fonts.googleapis.com/css2?family=Work+Sans:wght@400;500;600&display=swap" rel="stylesheet">
<style>
  :root {
    --bg: #161616;
    --card: #262626;
    --card-light: #2e2e2e;
    --white: #f4f4f4;
    --soft: #d9d9d9;
    --blue: #1ea6e6;
  }
  * { margin: 0; padding: 0; box-sizing: border-box; }
  html, body { width: 1200px; height: 900px; overflow: hidden; }
  body {
    background: var(--bg);
    font-family: "Work Sans", Arial, sans-serif;
    display: flex;
    flex-direction: column;
    align-items: center;
    justify-content: center;
    gap: 40px;
  }
  .card {
    position: relative;
    width: 700px;
    height: 390px;
    background: linear-gradient(135deg, var(--card) 0%, var(--card-light) 70%, var(--card) 100%);
    border-bottom: 6px solid var(--blue);
    overflow: hidden;
  }
  .wordmark {
    color: var(--white);
    font-weight: 600;
    letter-spacing: 0.12em;
    text-transform: uppercase;
    display: flex;
    align-items: center;
    gap: 14px;
    white-space: nowrap;
  }
  .wordmark .mark {
    width: 14px; height: 14px;
    background: var(--blue);
    flex: none;
  }
  .card-front { display: flex; align-items: center; justify-content: center; }
  .card-front .wordmark { font-size: 44px; }
  .card-back { display: flex; align-items: center; }
  .card-back .wordmark { font-size: 30px; position: absolute; left: 50px; top: 160px; }
  .divider {
    position: absolute;
    left: 395px; top: 85px;
    width: 2px; height: 210px;
    background: var(--soft);
  }
  .contact {
    position: absolute;
    left: 425px; top: 90px;
    color: var(--white);
  }
  .contact .name {
    color: var(--blue);
    font-size: 25px;
    font-weight: 500;
    letter-spacing: 0.06em;
    text-transform: uppercase;
  }
  .contact .role { font-size: 17px; margin-top: 2px; letter-spacing: 0.04em; }
  .contact .address { font-size: 16px; margin-top: 22px; line-height: 1.35; letter-spacing: 0.04em; }
  .contact .lines { list-style: none; margin-top: 16px; font-size: 16px; letter-spacing: 0.04em; }
  .contact .lines li { display: flex; align-items: center; gap: 10px; line-height: 1.6; }
  .contact .lines svg { width: 13px; height: 13px; flex: none; }
  .contact .accent { color: var(--blue); }
</style>
</head>
<body>
  <section class="card card-front">
    <div class="wordmark"><span class="mark"></span>Tessaron LLC</div>
  </section>

  <section class="card card-back">
    <div class="wordmark"><span class="mark"></span>Tessaron LLC</div>
    <div class="divider"></div>
    <div class="contact">
      <p class="name">Daniel Harlow</p>
      <p class="role">Director</p>
      <p class="address">418 Linden Avenue<br>Riverton, FL 32090</p>
      <ul class="lines">
        <li>
          <svg viewBox="0 0 16 16" fill="none" stroke="#1ea6e6" stroke-width="1.6"><path d="M4 1.5l2.5 3-1.5 1.5a9 9 0 0 0 5 5l1.5-1.5 3 2.5-1.5 2.5C7 14 2 9 1.5 3z"/></svg>
          555-014-2270
        </li>
        <li>
          <svg viewBox="0 0 16 16" fill="none" stroke="#1ea6e6" stroke-width="1.6"><rect x="1.5" y="3.5" width="13" height="9"/><path d="M1.5 3.5l6.5 5 6.5-5"/></svg>
          info@tessaronllc.com
        </li>
        <li>
          <svg viewBox="0 0 16 16" fill="none" stroke="#1ea6e6" stroke-width="1.4"><circle cx="8" cy="8" r="6.5"/><ellipse cx="8" cy="8" rx="2.8" ry="6.5"/><path d="M1.5 8h13M2.5 4.8h11M2.5 11.2h11"/></svg>
          <span>www.<span class="accent">tessaronllc</span>.com</span>
        </li>
      </ul>
    </div>
  </section>
</body>
</html>
```